Marlow Creek sign

24"x36" sign for new home construction job site. Located in affluent in-town neighborhood in Midwest. Traditional american style homes. 2nd generation construction company. Sign needs to convey strength and elegance but not overly elaborate. Competition most has signs consisting of text.

Sign text reads:
Marlow Creek Builders
Custom Luxury for Over 20 years
248-555-0137

Target Market(s)

Upper middle income home buyers

Industry/Entity Type

Construction

Font styles to use
Serif
Decorative

Requirements
Must have
• Logo image no more than 2 colors
Nice to have
• Should be visible and legible from distance of 30'
Should not have
• Not just image of house as logo

```html
<!DOCTYPE html>
<html lang="en">
<head>
<meta charset="utf-8">
<title>Marlow Creek Builders – Job Site Sign</title>
<link rel="stylesheet" href="https://fonts.googleapis.com/css2?family=Cinzel:wght@700&family=Cormorant+Garamond:wght@500&family=Open+Sans:wght@400&display=swap">
<style>
  :root {
    --maroon-core: #7d1819;
    --maroon-mid: #6a1416;
    --maroon-corner: #3a0204;
    --icon-maroon: #7a1a1c;
    --ink: #0d0d0d;
    --paper: #ffffff;
    --mark-fill: rgba(255, 255, 255, 0.18);
  }
  * { margin: 0; padding: 0; box-sizing: border-box; }
  html, body {
    width: 1200px;
    height: 1000px;
    overflow: hidden;
    background: var(--paper);
  }
  .sign {
    position: relative;
    width: 1200px;
    height: 1000px;
  }
  .sign-art {
    position: absolute;
    inset: 0;
  }
  .company-name {
    position: absolute;
    left: 0;
    width: 1184px;
    top: 418px;
    text-align: center;
    font-family: "Cormorant Garamond", Georgia, serif;
    font-weight: 500;
    font-size: 74px;
    line-height: 1;
    letter-spacing: 0;
    text-transform: uppercase;
    color: var(--paper);
  }
  .tagline {
    position: absolute;
    left: 0;
    width: 1184px;
    top: 580px;
    text-align: center;
    font-family: "Cinzel", "Times New Roman", serif;
    font-weight: 700;
    font-size: 49px;
    line-height: 1;
    letter-spacing: 1px;
    color: var(--ink);
  }
  .phone-line {
    position: absolute;
    left: 212px;
    top: 684px;
    display: flex;
    align-items: center;
    gap: 20px;
  }
  .phone-icon {
    width: 108px;
    height: 108px;
    flex: none;
  }
  .phone-number {
    font-family: "Open Sans", Arial, sans-serif;
    font-weight: 400;
    font-size: 80px;
    line-height: 1;
    letter-spacing: -1px;
    color: var(--ink);
  }
</style>
</head>
<body>
<main class="sign">
  <svg class="sign-art" width="1200" height="1000" viewBox="0 0 1200 1000">
    <defs>
      <radialGradient id="band-glow" cx="0.5" cy="0.5" r="0.65">
        <stop offset="0" stop-color="var(--maroon-core)"/>
        <stop offset="0.65" stop-color="var(--maroon-mid)"/>
        <stop offset="1" stop-color="var(--maroon-corner)"/>
      </radialGradient>
    </defs>
    <rect class="frame-outline" x="62" y="183" width="1056" height="688" fill="none" stroke="var(--ink)" stroke-width="3"/>
    <rect class="header-band" x="27" y="145" width="1130" height="381" fill="url(#band-glow)"/>
    <polyline class="frame-header-line" points="62,526 62,183 1118,183 1118,526" fill="none" stroke="var(--paper)" stroke-width="3"/>
    <rect class="logo-mark-slot" x="502" y="205" width="184" height="184" fill="var(--mark-fill)" role="img" aria-label="Company logo mark"/>
    <line class="name-rule-top" x1="352" y1="405" x2="832" y2="405" stroke="var(--paper)" stroke-width="3"/>
    <line class="name-rule-bottom" x1="355" y1="502" x2="834" y2="502" stroke="var(--paper)" stroke-width="3"/>
  </svg>

  <h1 class="company-name">Marlow Creek Builders</h1>

  <p class="tagline">Custom Luxury for Over 20 years</p>

  <div class="phone-line">
    <svg class="phone-icon" viewBox="0 0 108 108" aria-hidden="true">
      <path d="M30 92 A46 46 0 1 1 80 92" fill="none" stroke="var(--icon-maroon)" stroke-width="5"/>
      <path d="M62 22 l10 6 c3 2 3 5 1 8 l-7 10 c-2 3-5 3-7 2 l-4-2 c-5 8-9 17-11 26 l4 1 c3 1 4 3 4 6 l-2 12 c-1 3-3 5-6 4 l-10-3 c-6-20 6-52 28-70 z" fill="var(--icon-maroon)"/>
    </svg>
    <span class="phone-number">248-555-0137</span>
  </div>
</main>
</body>
</html>
```